Looking to Pick Up? Campaign

We are looking to design a double sided DL postcard to send to our clients to promote a new fixed cost recruitment service.
The theme of the campaign is to be 'Looking to Pick Up?'.
Attached is my own little mock up but I don't have the time or the skills to make something really impressionable.
Please note that the only things that need to be incorporated in this project from the draft that I've attached is the text (or similar) and our company logo.
if you need any royalty free mining pics or a gif of our logo, please email me, admin@tarnfield-staff.com
Any questions, please ask.
Cheers
Gwen
Updates
Dear Designers,
Please note that this design brief is for a double sided DL postcard. Some space must be left for a stamp & postage label on one side.
Secondly, the campaign is 'Looking to Pick Up', so risque / unique / memorable themes & graphics will be greatly appreciated.
Good luck!
Many thanks
Gwen

```html
<!DOCTYPE html>
<html lang="en">
<head>
<meta charset="utf-8">
<title>Looking to Pickup? – Tarnfield DL Postcard</title>
<link rel="stylesheet" href="https://fonts.googleapis.com/css2?family=Anton&family=Arimo:ital,wght@0,400;0,700;1,400;1,700&display=swap">
<style>
  :root {
    --board: #d9f0f4;
    --label: #8a8a8a;
    --card: #ffffff;
    --band: #0b0b0b;
    --steel: #5f84b0;
    --steel-dark: #1f3550;
    --red: #e01a1a;
    --ink: #111111;
    --grey-line: #c9c9c9;
    --brand: #b7b7b7;
    --brand-back: #9a9a9a;
    --accent: #e8c31c;
  }
  * { box-sizing: border-box; margin: 0; padding: 0; }
  html, body { width: 1200px; height: 911px; overflow: hidden; }
  body {
    position: relative;
    background: var(--board);
    font-family: "Arimo", Arial, sans-serif;
    color: var(--ink);
  }
  .side-label {
    position: absolute;
    font-size: 21px;
    color: var(--label);
  }
  .side-label--front { left: 994px; top: 180px; }
  .side-label--back { left: 98px; top: 630px; }

  .card {
    position: absolute;
    background: var(--card);
    box-shadow: 3px 4px 8px rgba(0,0,0,.35);
  }

  /* Front */
  .card--front { left: 83px; top: 22px; width: 874px; height: 411px; overflow: hidden; }
  .hero {
    position: absolute; left: 0; top: 0; width: 874px; height: 294px;
    background: linear-gradient(180deg, #9fb9d4 0%, #d6e1ea 45%, #e9ecec 62%, #b8ab92 82%, #8c7c62 100%);
  }
  .hero__haul-truck {
    position: absolute; left: 20px; top: 12px; width: 440px; height: 276px;
    border-radius: 6px;
    background: linear-gradient(160deg, #e2b43a 0%, #c9962a 40%, #6e5424 72%, #2a2620 100%);
  }
  .hero__pickup {
    position: absolute; left: 478px; top: 18px; width: 360px; height: 128px;
    border-radius: 6px;
    background: linear-gradient(180deg, #f2e35a 0%, #e0c92c 55%, #6a6450 100%);
  }
  .headline {
    position: absolute; left: 470px; top: 116px; width: 400px;
    font-family: "Anton", Impact, sans-serif;
    font-weight: 400;
    color: var(--steel);
    text-transform: uppercase;
    line-height: .85;
    -webkit-text-stroke: 1.5px #e8eef5;
    text-shadow: 2px 2px 0 var(--steel-dark), 4px 4px 0 var(--steel-dark), 6px 6px 6px rgba(0,0,0,.4);
  }
  .headline__top { display: block; font-size: 80px; padding-left: 8px; }
  .headline__top small { font-size: 50px; text-transform: lowercase; }
  .headline__main { display: block; font-size: 112px; }
  .band { position: absolute; left: 0; top: 294px; width: 874px; height: 117px; background: var(--band); }
  .brand {
    position: absolute;
    display: flex; align-items: center; gap: 6px;
    font-family: "Arimo", Arial, sans-serif; font-weight: 700;
    color: var(--brand); text-transform: uppercase;
  }
  .card--front .brand { left: 40px; top: 44px; font-size: 25px; }
  .brand__dot { width: 22px; height: 22px; border-radius: 50%; background: var(--accent); }
  .mine-photo { position: absolute; top: 11px; height: 94px; }
  .mine-photo--pit { left: 236px; width: 250px; background: linear-gradient(160deg, #2a1a0c, #b4631c 55%, #3a2410); }
  .mine-photo--night { left: 500px; width: 158px; background: linear-gradient(170deg, #141a2a, #a46a1e 60%, #2a1c10); }
  .mine-photo--plant { left: 668px; width: 192px; background: linear-gradient(180deg, #1a2a52, #3b4f8a 50%, #c48a2a 80%, #1c1c1c); }

  /* Back */
  .card--back { left: 184px; top: 469px; width: 942px; height: 424px; }
  .photo-strip {
    position: absolute; left: 24px; top: 9px; width: 464px; height: 77px;
    background: linear-gradient(90deg, #3f5e2c 0%, #7c8f5a 20%, #9aa7b8 30%, #6b6f78 48%, #c08a52 60%, #2a3a62 72%, #5c8ab8 86%, #aab4bc 100%);
  }
  .intro { position: absolute; left: 24px; top: 92px; width: 480px; font-size: 13.5px; line-height: 1.25; }
  .intro strong { font-size: 14.5px; }
  .service-title {
    position: absolute; left: 24px; top: 150px;
    font-family: "Anton", Impact, sans-serif; font-weight: 400; font-size: 26px; color: var(--red);
    text-transform: uppercase; letter-spacing: .2px;
    -webkit-text-stroke: 1.2px #000;
  }
  .price { position: absolute; left: 66px; display: flex; align-items: baseline; gap: 14px; }
  .price--standard { top: 190px; }
  .price--premium { top: 250px; }
  .price__amount { font-weight: 700; font-size: 30px; letter-spacing: -1px; }
  .price__amount sup { font-size: 8px; letter-spacing: 0; vertical-align: 18px; }
  .price__role { font-weight: 700; font-style: italic; font-size: 17px; }
  .upgrade {
    position: absolute; left: 60px; top: 290px; width: 440px;
    font-size: 12px; font-style: italic; font-weight: 700; text-align: center; line-height: 1.3;
  }
  .call-line {
    position: absolute; left: 24px; top: 333px;
    font-family: "Anton", Impact, sans-serif; font-size: 24px; color: var(--red);
    -webkit-text-stroke: 1px #000; text-transform: uppercase;
  }
  .fine-print {
    position: absolute; left: 24px; top: 368px; width: 870px;
    font-size: 5.6px; line-height: 1.35; color: #222;
  }
  .card--back .brand { left: 478px; top: 334px; font-size: 22px; color: var(--brand-back); }
  .social { position: absolute; left: 716px; top: 342px; display: flex; gap: 5px; }
  .social span { width: 13px; height: 13px; border-radius: 50%; background: var(--brand-back); }
  .address-note {
    position: absolute; left: 620px; top: 78px; width: 100px;
    font-size: 9px; text-align: center; line-height: 1.35; text-transform: uppercase;
  }
  .postage-box {
    position: absolute; left: 778px; top: 24px; width: 142px; height: 114px;
    border: 1px solid var(--grey-line);
    font-size: 9px; text-align: center; text-transform: uppercase; padding-top: 18px; line-height: 1.35;
  }
</style>
</head>
<body>
  <span class="side-label side-label--front">Front</span>
  <span class="side-label side-label--back">Back</span>

  <section class="card card--front" aria-label="Postcard front">
    <div class="hero" role="img" aria-label="Pale sky over a dusty mine site">
      <div class="hero__haul-truck" role="img" aria-label="Large yellow mine haul truck"></div>
      <div class="hero__pickup" role="img" aria-label="Classic yellow pickup truck"></div>
    </div>
    <h1 class="headline">
      <span class="headline__top">Looking <small>to</small></span>
      <span class="headline__main">Pickup?</span>
    </h1>
    <div class="band">
      <div class="brand"><span class="brand__dot"></span>Tarnfield</div>
      <div class="mine-photo mine-photo--pit" role="img" aria-label="Underground mine tunnel lit in orange"></div>
      <div class="mine-photo mine-photo--night" role="img" aria-label="Mining equipment working at night"></div>
      <div class="mine-photo mine-photo--plant" role="img" aria-label="Processing plant lit up at dusk"></div>
    </div>
  </section>

  <section class="card card--back" aria-label="Postcard back">
    <div class="photo-strip" role="img" aria-label="Strip of mining photos: drill rig, open pit, night site and surveyor"></div>
    <p class="intro"><strong>Upskill &amp; join the productivity crusade!</strong> Tarnfield, as mining's trusted talent acquisition partners are delighted to assist Aussie and Kiwi miners with rock bottom rates to help you pickup.</p>
    <h2 class="service-title">Specialist advertised &amp; network recruitment</h2>
    <div class="price price--standard">
      <span class="price__amount">$7K<sup>+ GST*</sup></span>
      <span class="price__role">Roles up to AU$150K fixed remuneration</span>
    </div>
    <div class="price price--premium">
      <span class="price__amount">$12K<sup>+ GST*</sup></span>
      <span class="price__role">Roles up to AU$150K to AU$200 TFR</span>
    </div>
    <p class="upgrade">Upgrade to premium ad package including Ore Weekly Pro.<br>Placement &amp; Careerlink Job slot for only $1600+ GST.</p>
    <p class="call-line">Pickup the best...call +617 3555 0142</p>
    <p class="fine-print">*Terms &amp; conditions apply. Rates quoted are per placement and exclude GST. Fixed fees cover roles advertised within Australia and New Zealand only. Premium packages include one featured listing, one network mailout and a thirty day job slot. Offer valid for new bookings made before the end of the financial year. Fees are payable on acceptance of offer by the candidate. Replacement guarantee applies for ninety days from start date where the candidate leaves for any reason. Candidates are sourced from our national mining network and verified before presentation. Advertising schedules are confirmed within two business days of booking. Pricing excludes travel and relocation costs. Tarnfield reserves the right to amend or withdraw this offer at any time without notice. Full terms available on request.</p>
    <div class="brand"><span class="brand__dot"></span>Tarnfield</div>
    <div class="social" aria-hidden="true"><span></span><span></span><span></span><span></span><span></span></div>
    <p class="address-note">This area<br>for<br>addresses</p>
    <div class="postage-box">Postage<br>here</div>
  </section>
</body>
</html>
```